Business card for consulting firm

We need a double-sided business card for consulting firm, VantoriX. The card should be professional but also creative and visually interesting.

Target Market(s)

Engineering and technology; transport industries; safety critical / heavy industry.

Contact Information for Business Card

See attached file with details.

Font styles to use
Sans Serif

```html
<!DOCTYPE html>
<html lang="en">
<head>
<meta charset="utf-8">
<title>VantoriX – Business Card</title>
<link rel="stylesheet" href="https://fonts.googleapis.com/css2?family=Roboto:wght@400;500;700&display=swap">
<style>
  :root {
    --page-bg: #2a2a2c;
    --navy-deep: #06051a;
    --ink: #221d4f;
    --purple: #8e3ea6;
    --purple-light: #b35bc9;
    --white: #ffffff;
    --grey-text: #3e3e48;
    --soft-text: #e6e3f0;
    --rule: #b9b6c8;
  }
  * { margin: 0; padding: 0; box-sizing: border-box; }
  html, body {
    width: 1200px; height: 1101px; overflow: hidden;
    background: var(--page-bg);
  }
  body {
    display: flex; flex-direction: column; align-items: center;
    gap: 39px; padding-top: 40px;
    font-family: "Roboto", Arial, sans-serif;
  }
  .card {
    position: relative; width: 860px; height: 491px; overflow: hidden;
    box-shadow: 0 10px 30px rgba(0,0,0,0.45);
  }

  .brand { display: flex; flex-direction: column; }
  .brand__name {
    font-family: "Roboto", Arial, sans-serif; font-weight: 700;
    text-transform: uppercase; letter-spacing: 4px; line-height: 1;
  }
  .brand__tagline {
    font-family: "Roboto", Arial, sans-serif; font-weight: 500;
    letter-spacing: 0.5px;
  }

  /* Back side */
  .card--back {
    background: radial-gradient(ellipse 45% 50% at 50% 47%, #2c1550 0%, #130d33 45%, var(--navy-deep) 100%);
    display: flex; align-items: center; justify-content: center;
  }
  .card--back .brand { align-items: center; }
  .card--back .brand__name { color: var(--white); font-size: 72px; }
  .card--back .brand__tagline { color: var(--white); font-size: 24px; margin-top: 12px; }

  /* Front side */
  .card--front { background: var(--white); }
  .front-art { position: absolute; inset: 0; width: 100%; height: 100%; }
  .card--front .brand {
    position: absolute; left: 72px; top: 80px; align-items: flex-start;
  }
  .card--front .brand__name { color: var(--ink); font-size: 76px; }
  .card--front .brand__tagline { color: var(--grey-text); font-size: 28px; margin-top: 12px; padding-left: 4px; }

  .person {
    position: absolute; right: 470px; top: 352px; text-align: right; color: var(--white);
  }
  .person__name { color: var(--purple-light); font-weight: 700; font-size: 25px; }
  .person__credentials { font-size: 13px; margin-top: 6px; color: var(--soft-text); }
  .person__role { font-size: 18px; font-weight: 700; margin-top: 6px; }

  .divider {
    position: absolute; left: 412px; top: 350px; width: 1px; height: 122px;
    background: var(--rule);
  }

  .contacts {
    position: absolute; left: 432px; top: 346px; list-style: none;
    display: flex; flex-direction: column; gap: 11px;
  }
  .contact { display: flex; align-items: center; gap: 12px; color: var(--white); font-size: 17px; }
  .contact__icon {
    width: 24px; height: 24px; border-radius: 50%; background: var(--purple);
    display: flex; align-items: center; justify-content: center; flex: none;
  }
  .contact__icon svg { width: 14px; height: 14px; }
</style>
</head>
<body>

  <section class="card card--back" aria-label="Card back">
    <div class="brand">
      <span class="brand__name">VantoriX</span>
      <span class="brand__tagline">Safety &amp; Human Factors</span>
    </div>
  </section>

  <section class="card card--front" aria-label="Card front">
    <svg class="front-art" viewBox="0 0 860 491" preserveAspectRatio="none" aria-hidden="true">
      <defs>
        <radialGradient id="panelGlow" cx="0.45" cy="0.85" r="0.6">
          <stop offset="0" stop-color="#2a1450"/>
          <stop offset="0.6" stop-color="#100b2e"/>
          <stop offset="1" stop-color="#07061b"/>
        </radialGradient>
        <linearGradient id="swoosh" x1="0" y1="0" x2="1" y2="0">
          <stop offset="0" stop-color="#b35bc9" stop-opacity="0.2"/>
          <stop offset="0.5" stop-color="#a44dbf"/>
          <stop offset="1" stop-color="#4b2d8f"/>
        </linearGradient>
      </defs>
      <path d="M0,345 C230,250 470,305 860,155 L860,491 L0,491 Z" fill="url(#panelGlow)"/>
      <path d="M330,292 C560,270 760,225 860,95 L860,155 C720,230 540,280 330,292 Z" fill="url(#swoosh)"/>
    </svg>

    <div class="brand">
      <span class="brand__name">VantoriX</span>
      <span class="brand__tagline">Safety &amp; Human Factors</span>
    </div>

    <div class="person">
      <div class="person__name">Helena Marsh</div>
      <div class="person__credentials">BA (Hons), M Psych Org, M Tech Mgt (HF)</div>
      <div class="person__role">Managing Director</div>
    </div>

    <div class="divider"></div>

    <ul class="contacts">
      <li class="contact">
        <span class="contact__icon"><svg viewBox="0 0 24 24"><path fill="#fff" d="M6.6 10.8a15.1 15.1 0 0 0 6.6 6.6l2.2-2.2c.3-.3.7-.4 1-.2 1.1.4 2.3.6 3.6.6.6 0 1 .4 1 1V20c0 .6-.4 1-1 1A17 17 0 0 1 3 4c0-.6.4-1 1-1h3.5c.6 0 1 .4 1 1 0 1.3.2 2.5.6 3.6.1.3 0 .7-.2 1z"/></svg></span>
        <span>+61 (0)400 555 018</span>
      </li>
      <li class="contact">
        <span class="contact__icon"><svg viewBox="0 0 24 24"><path fill="#fff" d="M3 6h18v12H3z"/><path fill="none" stroke="#8e3ea6" stroke-width="2" d="M3 6l9 7 9-7"/></svg></span>
        <span>hmarsh@vantorix.com.au</span>
      </li>
      <li class="contact">
        <span class="contact__icon"><svg viewBox="0 0 24 24" fill="none" stroke="#fff" stroke-width="1.8"><circle cx="12" cy="12" r="9"/><ellipse cx="12" cy="12" rx="4" ry="9"/><path d="M3 12h18"/></svg></span>
        <span>www.vantorix.global</span>
      </li>
      <li class="contact">
        <span class="contact__icon"><svg viewBox="0 0 24 24" fill="none" stroke="#fff" stroke-width="1.8"><circle cx="12" cy="12" r="9"/><ellipse cx="12" cy="12" rx="4" ry="9"/><path d="M3 12h18"/></svg></span>
        <span>www.vantorix.com.au</span>
      </li>
    </ul>
  </section>

</body>
</html>
```